Postcard Design-newbranchopening

Please refer to our website q7tutorhall.com.
We are opening a new Branch in Parsippany, NJ
Crest Score Pledge Program : 400 point increase or a score of 2200.
Sixteen real Crest Mock test.
Web Quiz Engine/Home Work.
Automatic test result analysis & Weak area detection.
Personal catchup Drill (PCD).
Perfect Score Students each year
Most of the students join based on reference
One time charge with no hidden or recurring fee
Free tuition and online system access until target reached

Main Message : $500 New Branch Open House DiscountComing in May 2015 in Parsippany, NJ Added Saturday, April 11, 2015

Target Market(s)

ASIAN Parents(Kids from 9th Grade to 11th Grade)

Colors
0355a3

Requirements
Must have
• Open House : $500 Discount Announcement
• Exam Prep Summer Camp (starts in July)
• 400 Point Increase or a score of 2200 (Refer to attached PDF from another branch)
• Weak area analysis and Personal Catchup Drill.
Nice to have
• Sixteen real Crest Mock test.
• 160 Hours of class.
• Weeks of required home work before class starts

```html
<!DOCTYPE html>
<html lang="en">
<head>
<meta charset="utf-8">
<title>Q7 Tutor Hall – New Branch Open House</title>
<link href="https://fonts.googleapis.com/css2?family=Schoolbell&family=Arimo:wght@400;700&display=swap" rel="stylesheet">
<style>
  :root {
    --board-deep: #123a66;
    --board-mid: #1b4c80;
    --board-light: #245a92;
    --band: #ffffff;
    --brand-blue: #1d5ea9;
    --chalk: #f4f4f0;
    --chalk-yellow: #f3ea3a;
    --chalk-area-a: #e9e4a8;
    --chalk-area-b: #d99a9c;
  }
  html, body {
    margin: 0;
    padding: 0;
    overflow: hidden;
    background: var(--board-deep);
  }
  .postcard {
    position: relative;
    width: 1200px;
    height: 863px;
    overflow: hidden;
    background: radial-gradient(ellipse at 55% 40%, var(--board-light) 0%, var(--board-mid) 45%, var(--board-deep) 100%);
    font-family: "Schoolbell", cursive;
  }
  .header-band {
    position: absolute;
    left: 130px;
    top: 94px;
    width: 1070px;
    height: 114px;
    background: var(--band);
  }
  .header-title,
  .header-offer {
    position: absolute;
    margin: 0;
    font-family: "Arimo", Arial, sans-serif;
    color: var(--brand-blue);
    white-space: nowrap;
    line-height: 1;
  }
  .header-title {
    left: 300px;
    top: 110px;
    font-size: 36px;
    font-weight: 700;
  }
  .header-offer {
    left: 294px;
    top: 155px;
    font-size: 32.5px;
    font-weight: 400;
  }
  .brand-seal {
    position: absolute;
    left: 37px;
    top: 12px;
    width: 256px;
    height: 256px;
    border-radius: 50%;
    background: var(--band);
    display: flex;
    align-items: center;
    justify-content: center;
  }
  .brand-name {
    font-family: "Arimo", Arial, sans-serif;
    font-weight: 700;
    font-size: 30px;
    color: var(--brand-blue);
    text-align: center;
    line-height: 1.15;
  }
  .feature-list {
    position: absolute;
    left: 300px;
    top: 266px;
    margin: 0;
    padding: 0;
    list-style: none;
    color: var(--chalk);
    font-size: 37px;
    line-height: 42px;
    letter-spacing: 0.5px;
  }
  .feature-list li { position: absolute; left: 0; white-space: nowrap; }
  .feature-camp { top: 0; }
  .feature-increase { top: 68px; }
  .feature-analysis { top: 138px; }
  .feature-tests { top: 253px; }
  .feature-hours { top: 333px; }
  .feature-homework { top: 428px; }
  .camp-start {
    color: var(--chalk-yellow);
    font-size: 29px;
  }
  .chalk-sticks {
    position: absolute;
    left: 20px;
    top: 460px;
    width: 200px;
    height: 380px;
    border-radius: 14px;
    opacity: 0.55;
    background: linear-gradient(160deg, var(--chalk-area-a) 0%, var(--chalk) 50%, var(--chalk-area-b) 100%);
  }
</style>
</head>
<body>
<main class="postcard">
  <div class="header-band"></div>
  <h1 class="header-title">New Branch Open House</h1>
  <p class="header-offer">$500&nbsp; Discount Coming in May 2015 in Parsippany, NJ</p>

  <div class="brand-seal">
    <span class="brand-name">Q7 Tutor<br>Hall</span>
  </div>

  <ul class="feature-list">
    <li class="feature-camp">Exam Prep Summer Camp <span class="camp-start">starts in July</span></li>
    <li class="feature-increase">400 Point Increase or a score of 2200</li>
    <li class="feature-analysis">Weak area analysis and Personal<br>Catchup Drill</li>
    <li class="feature-tests">Sixteen real Crest Mock test</li>
    <li class="feature-hours">160 Hours of class</li>
    <li class="feature-homework">Weeks of required home work<br>before class starts</li>
  </ul>

  <div class="chalk-sticks" role="img" aria-label="Three sticks of chalk in yellow, white and pink lying diagonally"></div>
</main>
</body>
</html>
```